RLTP Business Card Design

I have a rough idea of the design / layout of the company business card but need help in finalizing the design and quality.

I'm looking for the card to be stand out, but simple, on the front with clear detail on the back with space for some one to write any other detail they need onto the card. The rough draft includes the crinkled graph paper back ground which I quite like for the front.

I will need the card design completed and ready to print in Australian business card standard sizes. This includes detail on all colors, fonts and type faces used as well as copy of the original for editing (inserting other employee details).

I have included the company logo and a rough draft of the card, including the graphic I would like to use for the back ground on the front, I am not sure that the graphic is any good for printing, not the highest res.

Thanks,

Owen

```html
<!DOCTYPE html>
<html lang="en">
<head>
<meta charset="utf-8">
<title>RLTP Business Card</title>
<link rel="stylesheet" href="https://fonts.googleapis.com/css2?family=Barlow:wght@300;400;500&family=Barlow+Semi+Condensed:wght@400&display=swap">
<style>
  :root {
    --page: #ffffff;
    --card-dark: #0c0c0c;
    --card-mid: #2b2b2b;
    --card-glow: #3a3a3a;
    --card-green: rgba(40, 70, 45, 0.35);
    --ink-white: #f4f4f4;
    --ink-soft: #d6d6d6;
    --ink-muted: #7a7a7a;
    --ink-faint: #5e5e5e;
  }
  * { box-sizing: border-box; margin: 0; padding: 0; }
  html, body {
    width: 1200px;
    height: 669px;
    overflow: hidden;
    background: var(--page);
  }
  .canvas {
    position: relative;
    width: 1200px;
    height: 669px;
  }
  .card {
    position: absolute;
    left: 30px;
    width: 423px;
    height: 261px;
    overflow: hidden;
    background:
      radial-gradient(ellipse 70% 90% at 55% 10%, var(--card-glow) 0%, var(--card-mid) 30%, transparent 75%),
      radial-gradient(ellipse 45% 40% at 35% 95%, var(--card-green) 0%, transparent 100%),
      var(--card-dark);
    box-shadow: 1px 2px 4px rgba(0, 0, 0, 0.45);
    font-family: "Barlow", Arial, sans-serif;
    color: var(--ink-white);
  }
  .card--front { top: 30px; }
  .card--back { top: 341px; }
  .card__arcs {
    position: absolute;
    inset: 0;
    width: 100%;
    height: 100%;
  }
  .brand-name {
    position: absolute;
    font-family: "Barlow", Arial, sans-serif;
    font-weight: 500;
    color: var(--ink-white);
    letter-spacing: 0.02em;
    line-height: 1;
  }
  .card--front .brand-name {
    left: 0;
    right: 0;
    top: 62px;
    text-align: center;
    font-size: 112px;
  }
  .card--back .brand-name {
    left: 24px;
    top: 26px;
    font-size: 56px;
  }
  .contact {
    position: absolute;
    right: 28px;
    top: 86px;
    text-align: right;
    font-family: "Barlow Semi Condensed", Arial, sans-serif;
  }
  .contact__name {
    font-size: 20px;
    font-weight: 400;
    color: var(--ink-white);
    line-height: 1.1;
  }
  .contact__role {
    font-size: 8px;
    color: var(--ink-muted);
    letter-spacing: 0.04em;
    margin-bottom: 8px;
  }
  .contact__line {
    font-size: 12px;
    line-height: 19px;
    color: var(--ink-soft);
  }
  .address {
    position: absolute;
    left: 47px;
    top: 209px;
    font-family: "Barlow Semi Condensed", Arial, sans-serif;
    font-size: 13px;
    color: var(--ink-faint);
    letter-spacing: 0.02em;
  }
</style>
</head>
<body>
<main class="canvas">

  <section class="card card--front" aria-label="Card front">
    <svg class="card__arcs" viewBox="0 0 423 261" aria-hidden="true">
      <path d="M150 0 C 320 60, 360 170, 300 261" fill="none" stroke="rgba(255,255,255,0.04)" stroke-width="40"/>
      <path d="M250 0 C 390 70, 420 150, 423 200" fill="none" stroke="rgba(255,255,255,0.03)" stroke-width="30"/>
    </svg>
    <div class="brand-name">RLTP</div>
  </section>

  <section class="card card--back" aria-label="Card back">
    <svg class="card__arcs" viewBox="0 0 423 261" aria-hidden="true">
      <path d="M180 0 C 330 60, 350 170, 290 261" fill="none" stroke="rgba(255,255,255,0.04)" stroke-width="40"/>
      <path d="M270 0 C 390 70, 420 150, 423 200" fill="none" stroke="rgba(255,255,255,0.03)" stroke-width="30"/>
    </svg>
    <div class="brand-name">RLTP</div>
    <div class="contact">
      <div class="contact__name">Sam Carter</div>
      <div class="contact__role">CEO</div>
      <div class="contact__line">T: 0412 555 019</div>
      <div class="contact__line">F: 02 5550 1834</div>
      <div class="contact__line">E: hello@samcarter.com.au</div>
      <div class="contact__line">www.samcarter.com.au</div>
    </div>
    <div class="address">88 Harbourline Street, Marrickdale, Sydney 2099 NSW</div>
  </section>

</main>
</body>
</html>
```